Mobile Oil Change company needs a flyer to promote new business

We need a flyer to 1) print & handout and 2) email out to potential customers. We are a mobile oil change company that comes to our customer locations to perform the work instead of customers going to traditional oil change companies. We have a 21 point inspection with our oil change. (21 point inspection details will not be on the flyer). Would like to keep the flyer simple but creative. I'm attaching 1) the write-up we created, 2) our logo (logo color is dark teal on white but other combinations are included if you wanted to propose a different color combination), and 3) additional services we offer. Logo font is Alegreya Sans.
Would like the additional services listed with icons and brief descriptions (similar to attachment) without pricing. Company website for reference is www.brindlefleetcare.com.

Target Market(s)

Companies with many service vehicles such as Oil & Gas service companies, heating and air conditioning companies, utility companies, police departments, etc. Companies that prioritize convenience and maintenance first.

Font styles to use
Sans Serif

Colors
00a990

Requirements
Must have
• Simple but creative design with our logo at top of the flyer. Additional Services (details in document supplied) can be smaller and less prominent than other "main" content listed in the CONTENT document supplied.
Should not have
• Do not use animated character graphics in the flyer and limit (1) stock photos to A small area in the flyer.

```html
<!DOCTYPE html>
<html lang="en">
<head>
<meta charset="utf-8">
<title>Brindle Fleet Care – Mobile Oil Change Flyer</title>
<link rel="stylesheet" href="https://fonts.googleapis.com/css2?family=Alegreya+Sans:wght@800&family=Roboto:wght@400;500;700&display=swap">
<style>
  :root{
    --ink-teal:#17464c;
    --deep-teal:#1d4a4e;
    --bright-teal:#1ac3a9;
    --brand-teal:#00a990;
    --paper:#ffffff;
    --backdrop:#e1e1e1;
    --body-ink:#1f2f33;
  }
  *{box-sizing:border-box;margin:0;padding:0}
  html,body{width:1200px;height:1200px;overflow:hidden;background:var(--backdrop)}
  body{font-family:"Roboto",Arial,sans-serif;color:var(--body-ink)}
  .flyer{position:absolute;left:193px;top:30px;width:814px;height:1140px;background:var(--paper);overflow:hidden}
  .abs{position:absolute}

  .brand{left:0;width:814px;top:40px;text-align:center;color:var(--ink-teal);font-family:"Alegreya Sans",sans-serif;font-weight:800;line-height:1}
  .brand-name{font-size:66px;letter-spacing:1px}
  .brand-sub{font-size:19px;letter-spacing:5px;margin-top:6px}

  .headline{left:0;width:814px;text-align:center;font-family:"Alegreya Sans",sans-serif;font-weight:800;line-height:1}
  .headline-top{top:152px;font-size:57px;color:var(--ink-teal)}
  .headline-bottom{top:212px;font-size:57px;color:var(--brand-teal)}

  .photo{left:0;top:295px;width:350px;height:423px;background:linear-gradient(150deg,#b63a34 0%,#4a4f55 25%,#8b8f93 50%,#d9b62c 62%,#c9cdd1 80%,#6d7379 100%)}

  .process{left:374px;top:295px;width:440px;height:416px;background:var(--bright-teal);color:#fff}
  .process-strip{left:374px;top:705px;width:440px;height:8px;background:var(--deep-teal)}
  .process-intro{left:16px;top:30px;width:410px;font-size:25.5px;line-height:25px}
  .steps{left:0;top:0;width:440px;height:416px}
  .steps-line{left:33px;top:142px;width:2px;height:216px;background:var(--deep-teal)}
  .step{left:16px;width:410px;display:flex;align-items:center}
  .step-num{flex:0 0 35px;height:35px;border-radius:50%;background:var(--deep-teal);color:#fff;font-size:18px;display:flex;align-items:center;justify-content:center;border:2px solid var(--bright-teal);box-shadow:0 0 0 1px var(--deep-teal)}
  .step-text{margin-left:12px;font-size:18.5px;line-height:24px;font-weight:500}

  .services-title{left:32px;top:750px;font-size:23px;font-weight:700;color:var(--ink-teal)}
  .service-list{left:32px;top:788px;width:300px;list-style:none;font-size:17.5px;line-height:22px;font-weight:500}
  .service-list li{display:flex;margin-bottom:11px}
  .service-list svg{flex:0 0 22px;margin:3px 9px 0 0}

  .call-label{left:34px;top:978px;display:flex;align-items:center;font-size:26px;font-weight:500;color:var(--ink-teal)}
  .call-label svg{margin-right:14px}
  .phone-band{left:0;top:1015px;width:336px;height:57px;background:var(--bright-teal);color:#fff;font-size:33px;font-weight:500;padding-left:35px;line-height:57px}

  .extras{left:369px;top:733px;width:445px;height:291px;background:var(--deep-teal);color:#fff}
  .extras-title{left:21px;top:13px;font-size:20.5px;font-weight:700}
  .extra{width:171px;height:54px;border:1px solid rgba(255,255,255,.8);display:flex;align-items:center;padding-left:11px}
  .extra-icon{flex:0 0 40px;height:40px;border-radius:50%;background:#fff;display:flex;align-items:center;justify-content:center}
  .extra-label{margin-left:11px;font-size:13px;font-weight:700;line-height:16px}

  .footer-line{left:0;top:1093px;width:460px;height:5px;background:var(--bright-teal)}
  .footer-band{left:0;top:1100px;width:814px;height:18px;background:var(--deep-teal)}
  .contact{left:451px;top:1046px;width:363px;height:72px;background:var(--deep-teal);clip-path:polygon(18px 0,100% 0,100% 100%,0 100%);color:#fff;font-size:18.5px}
  .contact-row{position:absolute;left:53px;display:flex;align-items:center}
  .contact-row svg{margin-right:14px}
</style>
</head>
<body>
<div class="flyer">
  <div class="abs brand">
    <div class="brand-name">BRINDLE</div>
    <div class="brand-sub">FLEET CARE</div>
  </div>

  <h1 class="abs headline headline-top">HASSLE FREE OIL CHANGES</h1>
  <h2 class="abs headline headline-bottom">ON YOUR TERMS</h2>

  <div class="abs photo" role="img" aria-label="Photo of motor oil being poured through a yellow funnel into a car engine"></div>

  <section class="abs process">
    <p class="abs process-intro">Our simple 5-step process lets you schedule an appointment and get service to save time and money:</p>
    <div class="abs steps">
      <div class="abs steps-line"></div>
      <div class="abs step" style="top:125px"><span class="step-num">01</span><span class="step-text">Call or email us to schedule service</span></div>
      <div class="abs step" style="top:162px"><span class="step-num">02</span><span class="step-text">Our highly trained technicians come to you for service</span></div>
      <div class="abs step" style="top:220px"><span class="step-num">03</span><span class="step-text">Service is performed quickly on your vehicle</span></div>
      <div class="abs step" style="top:278px"><span class="step-num">04</span><span class="step-text">Pay agreed-upon pricing and receipt is emailed to you</span></div>
      <div class="abs step" style="top:336px"><span class="step-num">05</span><span class="step-text">Services performed are tracked electronically and reminders created</span></div>
    </div>
  </section>
  <div class="abs process-strip"></div>

  <h3 class="abs services-title">SERVICES</h3>
  <ul class="abs service-list">
    <li><svg width="20" height="16" viewBox="0 0 20 16"><path d="M2 8l5 5L18 2" fill="none" stroke="#1f2f33" stroke-width="2.6"/></svg><span>High quality synthetic oil used is best suited for commercial vehicles</span></li>
    <li><svg width="20" height="16" viewBox="0 0 20 16"><path d="M2 8l5 5L18 2" fill="none" stroke="#1f2f33" stroke-width="2.6"/></svg><span>Service includes a 21-point inspection</span></li>
    <li><svg width="20" height="16" viewBox="0 0 20 16"><path d="M2 8l5 5L18 2" fill="none" stroke="#1f2f33" stroke-width="2.6"/></svg><span>Additional services are available</span></li>
  </ul>

  <div class="abs call-label">
    <svg width="34" height="34" viewBox="0 0 34 34"><path d="M8 3l5 7-3 3c2 5 6 9 11 11l3-3 7 5-4 5C16 30 4 18 3 8z" fill="none" stroke="#1ac3a9" stroke-width="2.6"/><path d="M20 4a11 11 0 0 1 10 10M19 9a6 6 0 0 1 6 6" fill="none" stroke="#1ac3a9" stroke-width="2.4"/></svg>
    CALL NOW AT
  </div>
  <div class="abs phone-band">(833) 555-0147</div>

  <section class="abs extras">
    <h3 class="abs extras-title">Additional Services</h3>
    <div class="abs extra" style="left:21px;top:55px">
      <span class="extra-icon"><svg width="22" height="22" viewBox="0 0 22 22"><rect x="3" y="3" width="16" height="16" fill="#1ac3a9"/><path d="M7 3v16M11 3v16M15 3v16" stroke="#fff" stroke-width="1.2"/></svg></span>
      <span class="extra-label">Engine Air Filter Replacement</span>
    </div>
    <div class="abs extra" style="left:239px;top:55px">
      <span class="extra-icon"><svg width="22" height="22" viewBox="0 0 22 22"><rect x="4" y="3" width="14" height="16" fill="none" stroke="#1d4a4e" stroke-width="1.4"/><path d="M4 8h14M4 12h14M4 16h14" stroke="#1d4a4e" stroke-width="1.2"/></svg></span>
      <span class="extra-label">Cabin Air Filter Replacement</span>
    </div>
    <div class="abs extra" style="left:21px;top:134px">
      <span class="extra-icon"><svg width="22" height="22" viewBox="0 0 22 22"><path d="M3 8q8-6 16 0M11 19L4 9M11 19l7-10" fill="none" stroke="#1ac3a9" stroke-width="1.5"/></svg></span>
      <span class="extra-label">Wiperblade Replacement</span>
    </div>
    <div class="abs extra" style="left:239px;top:134px">
      <span class="extra-icon"><svg width="22" height="22" viewBox="0 0 22 22"><circle cx="11" cy="11" r="8" fill="none" stroke="#1ac3a9" stroke-width="1.6"/><circle cx="11" cy="11" r="3" fill="none" stroke="#1ac3a9" stroke-width="1.4"/><path d="M3 11h5M14 11h5M11 14v5" stroke="#1ac3a9" stroke-width="1.4"/></svg></span>
      <span class="extra-label">Power Steering Fluid Flush</span>
    </div>
    <div class="abs extra" style="left:21px;top:214px">
      <span class="extra-icon"><svg width="22" height="22" viewBox="0 0 22 22"><rect x="4" y="4" width="9" height="15" fill="none" stroke="#1d4a4e" stroke-width="1.4"/><path d="M6 8h5M13 8l4 3v6h-3" fill="none" stroke="#1d4a4e" stroke-width="1.3"/></svg></span>
      <span class="extra-label">Fuel System Treatment</span>
    </div>
    <div class="abs extra" style="left:239px;top:214px">
      <span class="extra-icon"><svg width="22" height="22" viewBox="0 0 22 22"><circle cx="11" cy="11" r="8" fill="none" stroke="#1ac3a9" stroke-width="1.6"/><circle cx="11" cy="11" r="4" fill="none" stroke="#1ac3a9" stroke-width="1.4"/><circle cx="11" cy="11" r="1.4" fill="#1ac3a9"/></svg></span>
      <span class="extra-label">Brake Fluid Flush</span>
    </div>
  </section>

  <div class="abs footer-line"></div>
  <div class="abs footer-band"></div>
  <div class="abs contact">
    <div class="contact-row" style="top:8px">
      <svg width="20" height="15" viewBox="0 0 20 15"><rect x="1" y="1" width="18" height="13" fill="none" stroke="#fff" stroke-width="1.4"/><path d="M1 1l9 7 9-7" fill="none" stroke="#fff" stroke-width="1.4"/></svg>
      Sales@BrindleFleetCare.com
    </div>
    <div class="contact-row" style="top:35px">
      <svg width="20" height="20" viewBox="0 0 20 20"><circle cx="10" cy="10" r="8.5" fill="none" stroke="#fff" stroke-width="1.4"/><ellipse cx="10" cy="10" rx="4" ry="8.5" fill="none" stroke="#fff" stroke-width="1.2"/><path d="M1.5 10h17M3 5.5h14M3 14.5h14" stroke="#fff" stroke-width="1.1"/></svg>
      www.brindlefleetcare.com
    </div>
  </div>
</div>
</body>
</html>
```